TALLYMORA (www.tallymora.com.zz) needs exciting professional Business Cards

TALLYMORA is an exciting new start-up targeting innovative ways to engage with retail customers at the point of sale.
Our Vision
Through applying new thinking to an old business we are reinventing selected segments of the Australian retail messaging industry, generating significant value for our customers, our suppliers, and our owners.
We operate with integrity, agility, and intelligence to doing things smarter, faster and more efficiently.
We bring deep industry expertise, deep relationships with customers and suppliers, and a will to see the old ways give way to smarter ways – this is why we win.
From this economically sustainable platform, we will examine the disruption of other market segments by further leveraging the elements that make us successful.
Our Values
With our clients, with our suppliers, with our staff, and with our owners:
# We Partner – We align the interest of all stakeholders by striving to ensure everything we do is mutually beneficial and commercially sustainable in the long term. We are clear with all our stakeholders about what our expectations are of them, and we seek clarity from them in their expectations of us.
# We Innovate – In the segments we choose to compete in, we bring fresh ideas, new business processes, the right relationships, and the right technology to ensure the supply chain is nimble, competitive, and reliable.
# We are Accountable – We say what we will do, and then do what we say.
# We Perform – We use our skills, relationships, and reputation to deliver value to our customers, suppliers, and owners.
Initially we are building our business from low-tech through printing promotional offers and retailer messages on ATM and EFTPOS receipts, but as soon as cash flow supports it we will be engaging in high-tech real-time targeted offers to the specific consumer.
I'd like the cards to reflect our values.
Please check out the web site we have just launched - it is pretty basic but it has only been up a week. We intend to sharpen it over the coming weeks, but you'll get the idea of what our core messages are.
I have recently sourced a logo from SketchHive, and have attached the source files for use.
Personal information to include:
Name: FirstName Surname
Title: Managing Director
email: first.surname@tallymora.com.zz
Mobile: +61-472-555-318
Generic Co Details to include:
Web: www.tallymora.com.zz
email: tallymora@tallymora.com.zz
Fax: +61-8-5037-2164
Offices & Agents: Sydney, Melbourne, Brisbane, Adelaide, Perth
Byline: Innovation . Integrity . Service
Target Market(s)
Our customers are large corporations that have professional Point Of Sale marketing experts looking for a supplier with an edge over others in a crowded market. The buyer of our product and services is ultimately a communications expert.
They want to see distinctive competence, and an agility of thinking that will make them money through driving more consumer spending.
Industry/Entity Type
Retail
Look and feel
Each slider illustrates characteristics of the customer's brand and the style your logo design should communicate.

```html
<!DOCTYPE html>
<html lang="en">
<head>
<meta charset="utf-8">
<title>TALLYMORA Business Cards</title>
<link rel="stylesheet" href="https://fonts.googleapis.com/css2?family=Open+Sans:wght@400;600;700&display=swap">
<style>
  :root {
    --brand-blue: #1b7fc4;
    --brand-blue-dark: #136aab;
    --brand-blue-light: #2a90d2;
    --charcoal: #3d4145;
    --ink: #4a4d50;
    --paper: #ffffff;
    --backdrop: #e4e5e6;
  }
  * { margin: 0; padding: 0; box-sizing: border-box; }
  html, body { width: 1200px; height: 999px; overflow: hidden; }
  body {
    background: var(--backdrop);
    font-family: "Open Sans", Arial, sans-serif;
    display: flex;
    align-items: center;
    justify-content: center;
    gap: 40px;
  }
  .card {
    position: relative;
    width: 540px;
    height: 309px;
    overflow: hidden;
    box-shadow: 0 6px 18px rgba(0,0,0,0.12);
  }
  /* Front */
  .card--front { background: var(--paper); color: var(--ink); }
  .card__band { position: absolute; inset: 0; width: 100%; height: 100%; }
  .brand {
    position: absolute;
    display: flex;
    align-items: center;
    gap: 8px;
    font-weight: 700;
    letter-spacing: 0.5px;
  }
  .card--front .brand { left: 34px; top: 70px; font-size: 30px; color: var(--brand-blue); }
  .brand__dot { border-radius: 50%; border: 2px solid currentColor; }
  .card--front .brand__dot { width: 22px; height: 22px; }
  .offices {
    position: absolute;
    left: 326px; top: 52px;
    font-size: 11.5px;
    line-height: 1.4;
  }
  .contact { list-style: none; }
  .contact li { display: flex; align-items: center; gap: 8px; font-size: 11.5px; line-height: 1.55; }
  .contact svg { width: 13px; height: 13px; flex: none; fill: var(--brand-blue); }
  .contact--company { position: absolute; left: 326px; top: 110px; }
  .person { position: absolute; left: 34px; top: 160px; }
  .person__name { font-size: 17px; font-weight: 600; color: var(--brand-blue); }
  .person__title { font-size: 11.5px; margin-bottom: 4px; }
  .web {
    position: absolute;
    right: 30px; top: 225px;
    display: flex; align-items: center; gap: 6px;
    font-size: 11.5px; color: var(--paper);
  }
  .web svg { width: 12px; height: 12px; fill: none; stroke: var(--paper); stroke-width: 1.3; }
  /* Back */
  .card--back {
    background: linear-gradient(135deg, var(--brand-blue-dark) 0%, var(--brand-blue) 55%, var(--brand-blue-light) 100%);
    color: var(--paper);
  }
  .card--back .brand { left: 50%; top: 100px; transform: translateX(-50%); font-size: 42px; gap: 12px; }
  .card--back .brand__dot { width: 34px; height: 34px; }
  .byline {
    position: absolute;
    left: 0; right: 0; top: 205px;
    text-align: center;
    font-size: 16px;
    letter-spacing: 0.4px;
  }
  .byline span::before { content: "\2022"; margin: 0 6px 0 14px; }
</style>
</head>
<body>

  <section class="card card--front" aria-label="Business card front">
    <svg class="card__band" viewBox="0 0 540 309" preserveAspectRatio="none" aria-hidden="true">
      <path d="M0 250 L290 250 C312 250 318 214 345 214 L540 214 L540 221 L348 221 C322 221 316 258 294 258 L0 258 Z" fill="var(--charcoal)"/>
      <path d="M0 258 L294 258 C316 258 322 221 348 221 L540 221 L540 309 L0 309 Z" fill="var(--brand-blue)"/>
    </svg>

    <div class="brand"><span>TALLYMORA</span><span class="brand__dot"></span></div>

    <p class="offices">Offices &amp; Agents:<br>Sydney, Melbourne<br>Brisbane, Adelaide, Perth</p>

    <ul class="contact contact--company">
      <li><svg viewBox="0 0 16 16" aria-hidden="true"><path d="M4 1h8v4H4zM1 6h14v7h-3v2H4v-2H1zM5 10v4h6v-4z"/></svg>: +61-8-5037-2164</li>
      <li><svg viewBox="0 0 16 16" aria-hidden="true"><path d="M1 3h14v10H1zM2 4.2v.6l6 4 6-4v-.6z"/></svg>: tallymora@tallymora.com.zz</li>
    </ul>

    <div class="person">
      <p class="person__name">Surname</p>
      <p class="person__title">Managing Director</p>
      <ul class="contact">
        <li><svg viewBox="0 0 16 16" aria-hidden="true"><path d="M1 3h14v10H1zM2 4.2v.6l6 4 6-4v-.6z"/></svg>first.surname@tallymora.com.zz</li>
        <li><svg viewBox="0 0 16 16" aria-hidden="true"><path d="M1 6c0-3 14-3 14 0v2h-4V6.5H5V8H1zM3 9h10l1 5H2z"/></svg>+61-472-555-318</li>
      </ul>
    </div>

    <p class="web"><svg viewBox="0 0 16 16" aria-hidden="true"><circle cx="8" cy="8" r="6.5"/><ellipse cx="8" cy="8" rx="3" ry="6.5"/><path d="M1.5 8h13"/></svg>www.tallymora.com.zz</p>
  </section>

  <section class="card card--back" aria-label="Business card back">
    <div class="brand"><span>TALLYMORA</span><span class="brand__dot"></span></div>
    <p class="byline"><span>Innovation</span><span>Integrity</span><span>Service</span></p>
  </section>

</body>
</html>
```